Providing Back Office Solutions to Financial Advisors and Attorney Needs a Business Card Design

Need a Business Card Design that speaks to Financial Advisor and Attorneys. Some of the word that come to mind is Clean/Simple & Futuristic.

Industry/Entity Type

Business

```html
<!DOCTYPE html>
<html lang="en">
<head>
<meta charset="utf-8">
<title>Novaris Business Card</title>
<link href="https://fonts.googleapis.com/css2?family=Montserrat:wght@300;400;600&display=swap" rel="stylesheet">
<style>
  :root {
    --page-bg: #e9e9ea;
    --card-center: #3a3b3d;
    --card-edge: #0f1011;
    --accent: #2a8fd0;
    --accent-soft: #4aa3dc;
    --ink-light: #f2f2f2;
    --ink-muted: #c9cdd2;
  }
  * { margin: 0; padding: 0; box-sizing: border-box; }
  html, body {
    width: 1200px; height: 900px; overflow: hidden;
    background: var(--page-bg);
    font-family: "Montserrat", Arial, sans-serif;
  }
  .canvas {
    width: 1200px; height: 900px;
    display: flex; align-items: center; justify-content: center;
  }
  .business-card {
    position: relative;
    width: 1000px; height: 572px;
    border-radius: 26px;
    background: radial-gradient(ellipse at 55% 40%, var(--card-center) 0%, #1d1e20 60%, var(--card-edge) 100%);
    overflow: hidden;
  }
  .brand {
    position: absolute; left: 78px; top: 62px;
    display: flex; align-items: center; gap: 22px;
  }
  .brand-mark {
    width: 70px; height: 70px;
    background: var(--accent);
    border-radius: 4px;
  }
  .brand-text { display: flex; flex-direction: column; gap: 6px; }
  .brand-name {
    font-weight: 600; font-size: 54px; letter-spacing: 4px;
    color: var(--accent); line-height: 1;
  }
  .brand-tagline {
    font-weight: 400; font-size: 17px; letter-spacing: 1.5px;
    color: var(--accent-soft);
  }
  .person {
    position: absolute; left: 78px; top: 200px;
  }
  .person-name {
    font-weight: 600; font-size: 48px; color: var(--accent); line-height: 1.05;
  }
  .person-title {
    font-weight: 400; font-size: 32px; color: var(--ink-light); line-height: 1.1;
  }
  .divider {
    position: absolute; left: 60px; right: 60px; top: 300px;
    height: 2px; background: var(--accent);
  }
  .contacts {
    position: absolute; left: 78px; top: 330px;
    list-style: none; display: flex; flex-direction: column; gap: 10px;
  }
  .contact-item {
    display: flex; align-items: center; gap: 14px;
    font-size: 24px; font-weight: 400; color: var(--ink-light);
  }
  .contact-icon { width: 22px; height: 22px; flex: none; }
  .address {
    position: absolute; right: 70px; bottom: 52px;
    text-align: right; font-size: 24px; line-height: 1.4;
    color: var(--ink-light); font-style: normal;
  }
</style>
</head>
<body>
<main class="canvas">
  <article class="business-card">
    <header class="brand">
      <div class="brand-mark" aria-hidden="true"></div>
      <div class="brand-text">
        <span class="brand-name">NOVARIS</span>
        <span class="brand-tagline">BACK OFFICE SOLUTIONS</span>
      </div>
    </header>

    <section class="person">
      <h1 class="person-name">Daniel Rourke</h1>
      <p class="person-title">President</p>
    </section>

    <div class="divider"></div>

    <ul class="contacts">
      <li class="contact-item">
        <svg class="contact-icon" viewBox="0 0 24 24" aria-hidden="true">
          <path fill="#2a8fd0" d="M6.6 10.8a15.1 15.1 0 0 0 6.6 6.6l2.2-2.2a1 1 0 0 1 1-.25 11.4 11.4 0 0 0 3.6.57 1 1 0 0 1 1 1V20a1 1 0 0 1-1 1A17 17 0 0 1 3 4a1 1 0 0 1 1-1h3.5a1 1 0 0 1 1 1c0 1.25.2 2.45.57 3.6a1 1 0 0 1-.25 1z"/>
        </svg>
        555 014 2280
      </li>
      <li class="contact-item">
        <svg class="contact-icon" viewBox="0 0 24 24" aria-hidden="true">
          <rect x="2" y="5" width="20" height="14" rx="1.5" fill="#2a8fd0"/>
          <path d="M2.5 6 12 13l9.5-7" fill="none" stroke="#151617" stroke-width="1.6"/>
        </svg>
        info@novarisbo.com
      </li>
      <li class="contact-item">
        <svg class="contact-icon" viewBox="0 0 24 24" aria-hidden="true">
          <g fill="none" stroke="#2a8fd0" stroke-width="1.8">
            <circle cx="12" cy="12" r="9.5"/>
            <ellipse cx="12" cy="12" rx="4.2" ry="9.5"/>
            <path d="M2.5 12h19M4 7h16M4 17h16"/>
          </g>
        </svg>
        www.novarisbo.com
      </li>
    </ul>

    <address class="address">
      42 Harbour Crest Avenue<br>
      Melbourne 3000
    </address>
  </article>
</main>
</body>
</html>
```